Crest Path Profile Bacground Needed

I need a simple Crest Path Background graphic for my Crest Path profile. My website is www.MorvexBLD.com
I have attached a couple of photos and our logo.

The tag line is: CRAFT | COMFORT | ON SCHEDULE | IN SCOPE

```html
<!DOCTYPE html>
<html lang="en">
<head>
<meta charset="utf-8">
<title>Crest Path Profile Background – Morvex Build</title>
<link rel="stylesheet" href="https://fonts.googleapis.com/css2?family=Montserrat:wght@500&display=swap">
<style>
  :root {
    --page-bg: #e6e6e6;
    --ink-black: #000000;
    --ink-white: #ffffff;
    --kitchen-light: #e9e2d8;
    --kitchen-mid: #c9ab86;
    --kitchen-dark: #8a6a4a;
    --bath-light: #f1ece4;
    --bath-mid: #ddd2c2;
    --bath-dark: #b9a58c;
  }
  html, body {
    margin: 0;
    padding: 0;
    width: 1200px;
    height: 849px;
    overflow: hidden;
    background: var(--page-bg);
  }
  .canvas {
    position: relative;
    width: 1200px;
    height: 849px;
  }
  .profile-banner {
    position: absolute;
    left: 40px;
    top: 250px;
    width: 1120px;
    height: 280px;
  }
  .tagline {
    position: absolute;
    left: 122px;
    top: 304px;
    margin: 0;
    font-family: "Montserrat", sans-serif;
    font-weight: 500;
    font-size: 15px;
    letter-spacing: 0.12em;
    color: var(--ink-white);
    white-space: nowrap;
  }
  .brand-badge {
    position: absolute;
    left: 120px;
    top: 368px;
    width: 230px;
    height: 230px;
    border-radius: 50%;
    background: var(--ink-black);
    box-shadow: 0 0 0 5px var(--ink-white);
    display: flex;
    align-items: center;
    justify-content: center;
  }
  .brand-name {
    font-family: "Montserrat", sans-serif;
    font-weight: 500;
    font-size: 21px;
    letter-spacing: 0.06em;
    color: var(--ink-white);
    white-space: nowrap;
  }
</style>
</head>
<body>
<main class="canvas">
  <svg class="profile-banner" viewBox="0 0 1120 280" width="1120" height="280">
    <defs>
      <linearGradient id="kitchen-tone" x1="0" y1="0" x2="0" y2="1">
        <stop offset="0" stop-color="#e9e2d8"/>
        <stop offset="0.55" stop-color="#c9ab86"/>
        <stop offset="1" stop-color="#8a6a4a"/>
      </linearGradient>
      <linearGradient id="bath-tone" x1="0" y1="0" x2="1" y2="1">
        <stop offset="0" stop-color="#b9a58c"/>
        <stop offset="0.45" stop-color="#ddd2c2"/>
        <stop offset="1" stop-color="#f1ece4"/>
      </linearGradient>
    </defs>
    <g role="img" aria-label="Photo of a finished open-plan kitchen and dining room with timber table and bar stools">
      <polygon points="549,0 878,0 797,280 464,280" fill="url(#kitchen-tone)"/>
    </g>
    <g role="img" aria-label="Photo of a renovated bathroom with walk-in shower, vanity and potted plants">
      <polygon points="888,0 1120,0 1120,280 808,280" fill="url(#bath-tone)"/>
    </g>
    <polygon class="banner-black" points="0,0 549,0 464,280 0,280" fill="#000000"/>
    <polygon class="banner-divider" points="868,0 888,0 809,280 787,280" fill="#000000"/>
  </svg>

  <p class="tagline">CRAFT | COMFORT | ON SCHEDULE | IN SCOPE</p>

  <div class="brand-badge">
    <span class="brand-name">MORVEX BUILD</span>
  </div>
</main>
</body>
</html>
```